Crestline Pools New website

I currently operate a swimming pool service and repair business and looking for a re design for my website as it has been over 5 years since it was designed. current site is crestlinepoolsqv.com

```html
<!DOCTYPE html>
<html lang="en">
<head>
<meta charset="utf-8">
<title>Crestline Pools</title>
<link href="https://fonts.googleapis.com/css2?family=Montserrat:wght@600;700&family=Roboto:wght@400;500;700&display=swap" rel="stylesheet">
<style>
:root{
  --navy:#0f1836;
  --navy-deep:#0b1230;
  --orange:#fb8c00;
  --sky:#e1f5fd;
  --accent:#1e90d6;
  --text:#333a44;
  --muted:#5b6470;
  --line:#d8dde3;
  --white:#ffffff;
}
*{margin:0;padding:0;box-sizing:border-box}
html,body{width:1200px;height:3011px;overflow:hidden}
body{font-family:"Roboto",sans-serif;color:var(--text);background:var(--white);position:relative}
section,header,footer{position:absolute;left:0;width:1200px}
.abs{position:absolute}
.photo{position:absolute;border-radius:10px}
.btn{position:absolute;background:var(--orange);color:var(--white);font-family:"Roboto",sans-serif;font-weight:700;font-size:16px;letter-spacing:.5px;border-radius:24px;display:flex;align-items:center;justify-content:center;text-transform:uppercase}
.h2{font-family:"Montserrat",sans-serif;font-weight:700;color:var(--navy);font-size:36px}
.brand{font-family:"Roboto",sans-serif;font-weight:700;font-size:22px;color:var(--white);display:flex;align-items:center;gap:8px}
.brand .dot{width:14px;height:14px;border-radius:50%;background:var(--orange)}
.icon-circle{position:absolute;border-radius:50%;display:flex;align-items:center;justify-content:center}

/* hero */
.hero{top:0;height:567px;background:linear-gradient(180deg,#1b2236 0%,#3a3426 45%,#2a3036 75%,#162033 100%)}
.nav{position:absolute;top:52px;left:62px;display:flex;gap:28px;font-size:13px;font-weight:500;color:var(--white)}
.nav .active{color:var(--orange);border-bottom:2px solid var(--orange);padding-bottom:4px}
.hero .brand{position:absolute;left:520px;top:44px}
.contact-top{position:absolute;top:38px;display:flex;gap:12px;align-items:flex-start}
.contact-top .lbl{color:var(--accent);font-size:14px}
.contact-top .val{color:var(--white);font-size:15px;font-weight:500}
.hero-title{left:62px;top:192px;font-family:"Montserrat",sans-serif;font-weight:700;font-size:50px;color:var(--white)}
.hero-sub{left:62px;top:264px;font-size:22px;font-weight:500;color:var(--white)}
.arrow-btn{position:absolute;top:292px;width:40px;height:40px;background:rgba(255,255,255,.18);border-radius:4px;display:flex;align-items:center;justify-content:center}

/* welcome */
.welcome{top:567px;height:408px}
.welcome p{position:absolute;left:63px;top:82px;width:525px;font-size:12.2px;line-height:18.7px;color:var(--text)}
.welcome a{color:var(--orange)}

/* services */
.services{top:975px;height:600px;background:var(--sky)}
.card{position:absolute;top:114px;width:343px;height:368px;background:var(--white);border-radius:10px;box-shadow:0 4px 14px rgba(0,0,0,.06)}
.card .num{position:absolute;left:14px;top:14px;font-family:"Montserrat",sans-serif;font-weight:600;font-size:60px;color:transparent;-webkit-text-stroke:1.3px #c9ced6;line-height:1}
.card .name{position:absolute;left:16px;top:88px;font-family:"Montserrat",sans-serif;font-weight:600;font-size:29px;color:var(--navy)}
.card .photo{left:16px;top:141px;width:311px;height:205px}
.card svg{position:absolute;right:14px;top:24px}
.dots{position:absolute;top:537px;left:564px;display:flex;gap:6px}
.dots span{width:18px;height:6px;border-radius:3px;background:#b6c4cf}
.dots span.on{background:var(--orange)}

/* why */
.why{top:1575px;height:571px}
.why .intro{position:absolute;left:609px;top:110px;width:530px;font-size:12.2px;line-height:18.7px;color:var(--muted)}
.feature{position:absolute;left:609px;top:219px;width:530px;height:112px;border:1px solid var(--line);border-radius:10px}
.feature .ic{position:absolute;left:20px;top:17px;width:78px;height:78px;background:var(--navy);border-radius:8px;display:flex;align-items:center;justify-content:center}
.feature .tx{position:absolute;left:112px;top:28px;font-size:19px;line-height:26px;color:var(--navy)}
.ticks{position:absolute;left:609px;top:364px;font-size:12.5px;color:var(--text)}
.ticks div{display:flex;align-items:center;gap:10px;height:23px}

/* contact */
.contact{top:2146px;height:480px;background:linear-gradient(180deg,#1e2639 0%,#2b3140 50%,#161d2e 100%)}
.contact .h2{color:var(--white);position:absolute;left:62px;top:40px}
.citem{position:absolute;left:62px;display:flex;gap:12px;align-items:flex-start}
.citem .lbl{color:var(--accent);font-size:15px}
.citem .val{color:var(--white);font-size:15px}
.form{position:absolute;left:647px;top:0;width:418px;height:433px;background:var(--white);border-radius:0 0 12px 12px}
.form label{position:absolute;font-size:12.5px;font-weight:700;color:var(--navy)}
.field{position:absolute;border:1px solid var(--line);border-radius:20px;font-size:12px;color:#8a9199;padding:0 14px;display:flex;align-items:center}
.captcha{position:absolute;left:17px;top:298px;width:189px;height:48px;background:#f9f9f9;border:1px solid #d3d3d3;font-size:8px;color:#222}

/* footer */
footer{top:2626px;height:385px;background:var(--navy-deep)}
footer .brand{position:absolute;left:0;width:1200px;justify-content:center;top:56px;font-size:26px}
.frule{position:absolute;left:172px;width:856px;height:1px;background:#2a3350}
.flinks{position:absolute;top:195px;left:0;width:1200px;display:flex;justify-content:center;gap:38px;font-size:12.5px;color:var(--white)}
.social{position:absolute;top:255px;left:555px;display:flex;gap:8px}
.social span{width:24px;height:24px;border-radius:50%;background:#2a3560}
.copy{position:absolute;top:343px;width:1200px;text-align:center;font-size:12.5px;color:var(--white)}
</style>
</head>
<body>

<header class="hero">
  <div class="photo" role="img" aria-label="Luxury home with lit patio and pool at dusk" style="inset:0;border-radius:0;background:linear-gradient(160deg,rgba(20,28,50,.7),rgba(120,95,55,.45) 45%,rgba(30,40,55,.7))"></div>
  <nav class="nav"><span class="active">HOME</span><span>ABOUT US</span><span>OUR SERVICES</span><span>FREE ESTIMATE</span><span>CONTACT</span></nav>
  <div class="brand"><span class="dot"></span>Crestline Pools</div>
  <div class="contact-top" style="left:762px">
    <div class="icon-circle" style="position:relative;width:38px;height:38px;background:#23345a">
      <svg width="18" height="18" viewBox="0 0 24 24" fill="none" stroke="#fff" stroke-width="1.6"><path d="M5 3h4l2 5-3 2a12 12 0 0 0 6 6l2-3 5 2v4a2 2 0 0 1-2 2A17 17 0 0 1 3 5a2 2 0 0 1 2-2z"/></svg>
    </div>
    <div><div class="lbl">Call us</div><div class="val">(702) 555-0148</div></div>
  </div>
  <div class="contact-top" style="left:950px">
    <div class="icon-circle" style="position:relative;width:38px;height:38px;background:#23345a">
      <svg width="18" height="18" viewBox="0 0 24 24" fill="none" stroke="#fff" stroke-width="1.6"><rect x="3" y="5" width="18" height="14" rx="2"/><path d="M3 7l9 6 9-6"/></svg>
    </div>
    <div><div class="lbl">Mail us</div><div class="val" style="font-size:13px;font-weight:400;line-height:16px">poolsolutions@<br>crestlinepoolsqv.com</div></div>
  </div>
  <div class="abs hero-title">WELCOME</div>
  <div class="abs hero-sub">Nevada’s Best Rated Local Pool Cleaning</div>
  <div class="btn" style="left:62px;top:319px;width:182px;height:44px">FREE ESTIMATE</div>
  <div class="arrow-btn" style="left:9px"><svg width="18" height="18" viewBox="0 0 24 24" fill="none" stroke="#fff" stroke-width="2.5"><path d="M20 12H5M11 5l-7 7 7 7"/></svg></div>
  <div class="arrow-btn" style="right:9px"><svg width="18" height="18" viewBox="0 0 24 24" fill="none" stroke="#fff" stroke-width="2.5"><path d="M4 12h15M13 5l7 7-7 7"/></svg></div>
  <svg class="abs" style="left:0;top:430px" width="1200" height="137" viewBox="0 0 1200 137">
    <path fill="#fff" d="M0 100 C40 80 60 20 110 16 C160 12 175 55 230 65 C300 75 330 35 380 40 C440 48 470 115 500 135 L500 137 L0 137Z"/>
    <path fill="#fff" d="M500 137 C520 80 540 50 620 52 C720 56 780 20 870 30 C960 40 1000 80 1060 60 C1120 40 1150 -5 1200 0 L1200 137Z"/>
    <ellipse cx="112" cy="85" rx="40" ry="20" transform="rotate(35 112 85)" fill="#131b35"/>
    <ellipse cx="930" cy="75" rx="46" ry="11" transform="rotate(-8 930 75)" fill="#131b35"/>
  </svg>
</header>

<section class="welcome">
  <div class="abs h2" style="left:63px;top:24px">Welcome</div>
  <p>When you need professional pool cleaning services in Nevada, you can count on the professionals at Crestline Pools to provide you with superior and prompt solutions. Whether you need assistance with a <a href="#">residential</a> or <a href="#">commercial</a> pool, we’ll vacuum, brush, and thoroughly clean your pool so it’s swim-ready. We’ll also clean your pool filters and inform you of any issues that arise. Our staff is certified by the Desert Valley Health District to ensure proper chemical levels and equipment are safe. To learn more about our pool cleaning services or to get your <a href="#">free estimate</a>, contact our pool experts today.</p>
  <div class="btn" style="left:62px;top:234px;width:182px;height:44px">FREE ESTIMATE</div>
  <div class="icon-circle" style="left:265px;top:234px;width:44px;height:44px;background:var(--navy)">
    <svg width="20" height="20" viewBox="0 0 24 24" fill="none" stroke="#fff" stroke-width="1.6"><path d="M5 3h4l2 5-3 2a12 12 0 0 0 6 6l2-3 5 2v4a2 2 0 0 1-2 2A17 17 0 0 1 3 5a2 2 0 0 1 2-2z"/></svg>
  </div>
  <div class="abs" style="left:319px;top:232px;font-size:17px;color:var(--accent)">Call us</div>
  <div class="abs" style="left:319px;top:257px;font-size:19px;color:var(--navy)">(702) 555-0148</div>
  <div class="photo" role="img" aria-label="Modern stone house with illuminated pool at dusk" style="left:721px;top:30px;width:416px;height:300px;background:linear-gradient(170deg,#7aa3d8 0%,#b49a78 35%,#3f6a80 65%,#1f4a5e 100%)"></div>
  <div class="photo" role="img" aria-label="Resort pool with thatched gazebo and palm trees" style="left:605px;top:179px;width:255px;height:176px;border:4px solid #fff;border-radius:12px;background:linear-gradient(170deg,#6fb6e6 0%,#5a8a4a 35%,#3aa6d6 65%,#1e86c0 100%)"></div>
</section>

<section class="services">
  <div class="abs h2" style="left:0;width:1200px;text-align:center;top:36px">Our Services</div>
  <div class="card" style="left:62px">
    <div class="num">01</div>
    <svg width="38" height="38" viewBox="0 0 38 38" fill="none" stroke="#7d8690" stroke-width="2"><path d="M4 34L34 4M14 4h20v20"/></svg>
    <div class="name">Pool Services</div>
    <div class="photo" role="img" aria-label="Backyard pool in front of a lit modern home at night" style="background:linear-gradient(180deg,#8a7a5e 0%,#c9a46a 40%,#1e2e58 70%,#0e1a40 100%)"></div>
  </div>
  <div class="card" style="left:428px">
    <div class="num">02</div>
    <svg width="38" height="38" viewBox="0 0 38 38" fill="none" stroke="#7d8690" stroke-width="2"><path d="M4 34L34 4M14 4h20v20"/></svg>
    <div class="name">Commercial Pools</div>
    <div class="photo" role="img" aria-label="Commercial pool with patio and flower planters" style="background:linear-gradient(160deg,#4d6a30 0%,#a07a5a 30%,#c9b9a8 50%,#2fa3c9 75%,#1b7fa8 100%)"></div>
  </div>
  <div class="card" style="left:793px">
    <div class="num">03</div>
    <svg width="38" height="38" viewBox="0 0 38 38" fill="none" stroke="#7d8690" stroke-width="2"><path d="M4 34L34 4M14 4h20v20"/></svg>
    <div class="name">Residential Pools</div>
    <div class="photo" role="img" aria-label="Rock-edged residential pool with a spa" style="background:linear-gradient(120deg,#6a3a1c 0%,#8a5a34 40%,#5fa6b8 70%,#8cc6d6 100%)"></div>
  </div>
  <div class="dots"><span class="on"></span><span></span><span></span></div>
</section>

<section class="why">
  <div class="abs h2" style="left:63px;top:51px">Why Choose Us?</div>
  <div class="photo" role="img" aria-label="Contemporary glass house with lit patio at dusk" style="left:62px;top:114px;width:489px;height:224px;background:linear-gradient(180deg,#3a5a9a 0%,#c9a060 45%,#6a7a8a 75%,#3a5070 100%)"></div>
  <div class="photo" role="img" aria-label="Indoor pool with tiled floor" style="left:62px;top:359px;width:209px;height:160px;background:linear-gradient(180deg,#3a4658 0%,#4fa8e0 45%,#2a8fd4 100%)"></div>
  <div class="photo" role="img" aria-label="Pool ladder over clear blue water beside brick deck" style="left:291px;top:359px;width:259px;height:160px;background:linear-gradient(120deg,#2e9ccc 0%,#56b8e0 55%,#a87a62 80%,#8a6450 100%)"></div>
  <div class="intro">Our full-service pool company proudly serves the entire Las Vegas valley, and we’re certified by the Desert Valley Health District to maintain the highest level of pool safety. If you need repairs, maintenance, scheduled cleanings, or any other pool services, contact us online or by phone today.</div>
  <div class="feature">
    <div class="ic"><svg width="46" height="46" viewBox="0 0 24 24" fill="none" stroke="#fff" stroke-width="1.2"><path d="M14 4l6 6M17 7l-7 7M6 11l7 7-4 3-6-6z"/><circle cx="5" cy="5" r=".8"/><circle cx="9" cy="3" r=".6"/><circle cx="18" cy="19" r="1"/></svg></div>
    <div class="tx">Custom Maintenance Plans Tailored to Your<br>Pool's Needs</div>
  </div>
  <div class="ticks">
    <div><svg width="18" height="10" viewBox="0 0 18 10" fill="none" stroke="#1e90d6" stroke-width="1.6"><path d="M1 5l3 3 6-7M7 8l1 0 8-7"/></svg>Custom Maintenance Plans Tailored to Your Pool's Needs</div>
    <div><svg width="18" height="10" viewBox="0 0 18 10" fill="none" stroke="#1e90d6" stroke-width="1.6"><path d="M1 5l3 3 6-7M7 8l1 0 8-7"/></svg>Using Eco-Friendly and Safe Cleaning Products for a Healthier Pool</div>
  </div>
  <div class="btn" style="left:609px;top:436px;width:163px;height:43px">CONTACT US</div>
</section>

<section class="contact">
  <div class="photo" role="img" aria-label="Poolside lounge area of a home at night" style="inset:0;border-radius:0;background:linear-gradient(180deg,rgba(20,28,45,.6),rgba(40,46,60,.4) 50%,rgba(15,22,40,.7))"></div>
  <div class="h2">Contact Us</div>
  <div class="citem" style="top:114px">
    <div class="icon-circle" style="position:relative;width:38px;height:38px;background:#1e6ea8"><svg width="18" height="18" viewBox="0 0 24 24" fill="none" stroke="#fff" stroke-width="1.6"><path d="M5 3h4l2 5-3 2a12 12 0 0 0 6 6l2-3 5 2v4a2 2 0 0 1-2 2A17 17 0 0 1 3 5a2 2 0 0 1 2-2z"/></svg></div>
    <div><div class="lbl">Call us</div><div class="val">(702) 555-0148</div></div>
  </div>
  <div class="citem" style="top:175px">
    <div class="icon-circle" style="position:relative;width:38px;height:38px;background:#1e6ea8"><svg width="18" height="18" viewBox="0 0 24 24" fill="none" stroke="#fff" stroke-width="1.6"><rect x="3" y="5" width="18" height="14" rx="2"/><path d="M3 7l9 6 9-6"/></svg></div>
    <div><div class="lbl">Mail us</div><div class="val">poolsolutions@crestlinepoolsqv.com</div></div>
  </div>
  <div class="form">
    <label style="left:19px;top:21px">Name</label>
    <div class="field" style="left:17px;top:40px;width:386px;height:41px">Name</div>
    <label style="left:19px;top:98px">Phone</label>
    <div class="field" style="left:17px;top:117px;width:188px;height:41px">Phone</div>
    <label style="left:215px;top:98px">Email</label>
    <div class="field" style="left:215px;top:117px;width:188px;height:41px">Email</div>
    <label style="left:17px;top:171px">Message</label>
    <div class="field" style="left:17px;top:194px;width:386px;height:86px;align-items:flex-start;padding-top:14px">Message</div>
    <div class="captcha">
      <div class="abs" style="left:9px;top:15px;width:17px;height:17px;border:2px solid #c1c1c1;background:#fff;border-radius:2px"></div>
      <div class="abs" style="left:33px;top:19px">I'm not a robot</div>
      <div class="abs" style="left:148px;top:9px;width:16px;height:16px;border-radius:50%;background:#9aa6b8"></div>
      <div class="abs" style="left:138px;top:29px;font-size:6px">VerifyBox</div>
      <div class="abs" style="left:138px;top:37px;font-size:5px;color:#666">Privacy - Terms</div>
    </div>
    <div class="btn" style="left:17px;top:363px;width:162px;height:43px">CONTACT US</div>
  </div>
</section>

<footer>
  <div class="brand"><span class="dot"></span>Crestline Pools</div>
  <div class="frule" style="top:175px"></div>
  <div class="flinks"><span>HOME</span><span>ABOUT US</span><span>OUR SERVICES</span><span>FREE ESTIMATE</span><span>CONTACT</span><span>BLOG</span><span>PRIVACY POLICY</span></div>
  <div class="frule" style="top:229px"></div>
  <div class="social"><span></span><span></span><span></span></div>
  <div class="copy">©2026 Crestline Pools - Do not copy. All rights reserved.</div>
</footer>

</body>
</html>
```